Tradeshow Exhibit Background Design

Looking to make improvements on my tradeshow exhibit backdrop. I created the current design myself, and I'm not 100% happy with it. Because its a big investment, I want it to be perfect.
For context:
- The booth will be used in multiple configurations (20 ft, 10 ft, and 8 ft).
- The booth structure will include two panels that are 5' x 7.5', and one panel that is 8' x 8.5' (attached a photo of the set-up.)
- We plan on getting the double sided fabric printing so that we can use it in the various configurations (the 10' config will be the two 5' panels put together, and the 20' config will be all three.)
The design should be visually impactful from a distance but also clear and readable up close. It needs to align with our brand identity and effectively communicate what we do at a glance.
I've includes a photo example of the booth structure, my current design, as well as our company brand guidelines.

```html
<!DOCTYPE html>
<html lang="en">
<head>
<meta charset="utf-8">
<title>Summitra Mining Solutions – Tradeshow Backdrop</title>
<link rel="stylesheet" href="https://fonts.googleapis.com/css2?family=Poppins:wght@400;500;700;800&family=Heebo:wght@400&display=swap">
<style>
  :root {
    --ink: #111;
    --panel-dark: #12262c;
    --panel-deep: #0d1e23;
    --white: #ffffff;
    --accent-red: #d6242f;
    --dim-line: #c5cedb;
    --grey-photo-light: #c9c9c9;
    --grey-photo-dark: #6d6f70;
    --truck-orange: #e8a233;
    --truck-shadow: #4a4a48;
    --muted: #b8bcbf;
  }
  * { margin: 0; padding: 0; box-sizing: border-box; }
  html, body { width: 1200px; height: 734px; overflow: hidden; background: var(--white); }
  .canvas { position: relative; width: 1200px; height: 734px; font-family: "Poppins", sans-serif; color: var(--ink); }

  /* dimension annotations */
  .dimension { position: absolute; }
  .dimension-label { position: absolute; font-family: "Poppins", sans-serif; font-size: 20px; color: var(--ink); transform: translateX(-50%); }

  /* panels */
  .panel { position: absolute; top: 181px; height: 403px; border-radius: 14px; overflow: hidden; background: var(--panel-dark); }
  .panel-left { left: 94px; width: 268px; }
  .panel-center { left: 363px; width: 428px; background: var(--grey-photo-dark); }
  .panel-right { left: 793px; width: 267px; }

  .stand-foot { position: absolute; left: 195px; top: 584px; width: 68px; height: 12px; background: #000; }

  .photo { position: absolute; left: 0; right: 0; }
  .photo-left-worker {
    top: 92px; bottom: 0;
    background: linear-gradient(160deg, #55646a 0%, #3b4b50 35%, #2a3a3f 65%, #5a4b3a 100%);
  }
  .photo-right-workers {
    top: 100px; bottom: 0;
    background: linear-gradient(200deg, #4b4036 0%, #6a4a2e 30%, #2e3a3e 65%, #3f4a3a 100%);
  }
  .photo-quarry {
    top: 0; bottom: 0;
    background: linear-gradient(180deg, var(--grey-photo-light) 0%, #9a9a9a 55%, var(--grey-photo-dark) 100%);
  }
  .photo-truck {
    position: absolute; left: 61px; top: 118px; width: 328px; height: 250px; border-radius: 6px;
    background: radial-gradient(ellipse at 60% 55%, var(--truck-orange) 0%, #c9862c 40%, var(--truck-shadow) 85%, transparent 100%);
  }

  .overlay { position: absolute; left: 0; top: 0; width: 100%; height: 100%; }

  .headline {
    position: absolute; left: 0; right: 0; top: 14px;
    text-align: center; color: var(--white);
    font-size: 29.5px; font-weight: 400; line-height: 33px;
  }

  .brand { position: absolute; display: flex; align-items: flex-start; color: var(--white); font-family: "Poppins", sans-serif; font-weight: 800; }
  .brand-name { letter-spacing: 1px; }
  .brand-dot { width: 7px; height: 7px; border-radius: 50%; background: var(--accent-red); margin-left: 3px; }
  .brand-center { left: 42px; top: 34px; font-size: 38px; line-height: 42px; }
  .brand-right { left: 0; right: 0; top: 28px; justify-content: center; font-size: 35px; line-height: 40px; }
  .brand-descriptor {
    position: absolute; left: 268px; top: 40px;
    font-family: "Poppins", sans-serif; font-weight: 700; font-size: 13.5px; line-height: 16px; color: var(--muted);
  }
  .tagline {
    position: absolute; left: 43px; top: 79px;
    font-family: "Heebo", sans-serif; font-size: 20px; color: var(--white); letter-spacing: 0.3px;
  }
  .web-address {
    position: absolute; left: 0; right: 0; bottom: 6px; text-align: center;
    font-size: 17.5px; font-weight: 500; color: var(--white); letter-spacing: 0.8px;
  }
</style>
</head>
<body>
<main class="canvas">

  <!-- dimension annotations -->
  <svg class="dimension" style="left:0;top:0" width="1200" height="734" aria-hidden="true">
    <g stroke="var(--dim-line)" stroke-width="2" fill="none">
      <line x1="96" y1="151" x2="365" y2="151"/><line x1="96" y1="146" x2="96" y2="156"/><line x1="365" y1="146" x2="365" y2="156"/>
      <line x1="792" y1="151" x2="1062" y2="151"/><line x1="792" y1="146" x2="792" y2="156"/><line x1="1062" y1="146" x2="1062" y2="156"/>
      <line x1="1095" y1="182" x2="1095" y2="595"/><line x1="1090" y1="182" x2="1100" y2="182"/><line x1="1090" y1="595" x2="1100" y2="595"/>
      <line x1="363" y1="625" x2="790" y2="625"/><line x1="363" y1="620" x2="363" y2="630"/><line x1="790" y1="620" x2="790" y2="630"/>
    </g>
  </svg>
  <span class="dimension-label" style="left:232px;top:120px">5′</span>
  <span class="dimension-label" style="left:928px;top:120px">5′</span>
  <span class="dimension-label" style="left:1126px;top:362px">7.5′</span>
  <span class="dimension-label" style="left:567px;top:634px">8′</span>

  <!-- left panel -->
  <section class="panel panel-left">
    <div class="photo photo-left-worker" role="img" aria-label="Photo of a miner in an orange hard hat and hi-vis jacket in a control room"></div>
    <svg class="overlay" viewBox="0 0 268 403" preserveAspectRatio="none" aria-hidden="true">
      <path d="M0 0 H268 V368 C150 368 20 300 0 120 Z" fill="var(--panel-dark)" opacity="0.55"/>
      <rect x="0" y="0" width="268" height="92" fill="var(--panel-dark)"/>
    </svg>
    <h2 class="headline">Lasting Gains<br>Proven Results</h2>
  </section>
  <div class="stand-foot"></div>

  <!-- center panel -->
  <section class="panel panel-center">
    <div class="photo photo-quarry" role="img" aria-label="Photo of an open-pit quarry in greyscale"></div>
    <svg class="overlay" viewBox="0 0 428 403" preserveAspectRatio="none" aria-hidden="true">
      <path d="M0 0 H402 C360 120 220 230 0 198 Z" fill="var(--panel-dark)"/>
      <path d="M402 0 C360 120 220 230 0 198" fill="none" stroke="var(--white)" stroke-width="5"/>
    </svg>
    <div class="photo-truck" role="img" aria-label="Photo of a yellow mining haul truck loaded with ore"></div>
    <div class="brand brand-center"><span class="brand-name">SUMMITRA</span><span class="brand-dot"></span></div>
    <div class="brand-descriptor">Mining<br>Solutions</div>
    <p class="tagline">BE THE SUMMIT</p>
    <p class="web-address">www.summitraminingsolutions.com</p>
  </section>

  <!-- right panel -->
  <section class="panel panel-right">
    <div class="photo photo-right-workers" role="img" aria-label="Photo of two smiling miners in orange hard hats"></div>
    <svg class="overlay" viewBox="0 0 267 403" preserveAspectRatio="none" aria-hidden="true">
      <path d="M0 0 H267 V115 C250 300 120 366 0 366 Z" fill="var(--panel-dark)" opacity="0.5"/>
      <rect x="0" y="0" width="267" height="100" fill="var(--panel-dark)"/>
    </svg>
    <div class="brand brand-right"><span class="brand-name">SUMMITRA</span><span class="brand-dot"></span></div>
  </section>

</main>
</body>
</html>
```